Business Card

I need a business card that really pops for a potential customer or person who refers a personal injury lead. I want to highlight our office locations, but only address that needs to be on the card is my office's main address. I want a sleek, modern and minimalist design.

```html
<!DOCTYPE html>
<html lang="en">
<head>
<meta charset="UTF-8">
<title>Northfield Injury Lawyers — Business Card</title>
<link href="https://fonts.googleapis.com/css2?family=Roboto:wght@400;700&display=swap" rel="stylesheet">
<style>
  :root {
    --backdrop: #cfcfcf;
    --card: #ffffff;
    --card-edge: #3a3a3a;
    --ink: #111111;
    --ink-soft: #2e2e2e;
    --muted: #8a8a8a;
  }
  * { box-sizing: border-box; margin: 0; padding: 0; }
  html, body {
    width: 1200px; height: 1200px; overflow: hidden;
    background: var(--backdrop);
    font-family: "Roboto", Arial, sans-serif;
  }
  .stage { position: relative; width: 1200px; height: 1200px; }
  .card {
    position: absolute; left: 300px;
    width: 600px; height: 343px;
    background: var(--card);
    border: 4px solid var(--card-edge);
    border-radius: 28px;
    box-shadow: 0 6px 14px rgba(0,0,0,0.18);
  }
  .card--front { top: 190px; }
  .card--back { top: 667px; }

  .brand {
    display: flex; align-items: center;
    color: var(--ink-soft); font-weight: 400; line-height: 1; white-space: nowrap;
  }
  .brand__square { flex: none; background: var(--ink-soft); }

  .card--front .brand { position: absolute; top: 34px; right: 34px; font-size: 18px; gap: 10px; }
  .card--front .brand__square { width: 12px; height: 12px; }

  .card--back .brand {
    position: absolute; top: 50%; left: 50%; transform: translate(-50%, -50%);
    font-size: 34px; gap: 18px;
  }
  .card--back .brand__square { width: 22px; height: 22px; }

  .identity {
    position: absolute; left: 0; top: 96px;
    padding-left: 36px;
  }
  .identity::before {
    content: ""; position: absolute; left: 0; top: 34px;
    width: 12px; height: 48px; background: var(--ink);
  }
  .identity__name { font-size: 26px; font-weight: 700; color: var(--ink); line-height: 30px; }
  .identity__title { font-size: 21px; color: var(--ink); margin-top: 2px; padding-left: 18px; line-height: 26px; }
  .identity__address { font-size: 17px; color: var(--muted); margin-top: 8px; padding-left: 40px; line-height: 23px; }

  .contacts { position: absolute; left: 60px; top: 222px; list-style: none; }
  .contacts li {
    display: flex; align-items: center; gap: 14px;
    font-size: 17px; color: var(--muted); height: 24px;
  }
  .contacts svg { width: 20px; height: 20px; flex: none; }
</style>
</head>
<body>
<main class="stage">
  <section class="card card--front" aria-label="Business card front">
    <div class="brand">
      <span class="brand__square" aria-hidden="true"></span>
      <span class="brand__name">Northfield Injury Lawyers</span>
    </div>
    <div class="identity">
      <p class="identity__name">HOLLIS, JR</p>
      <p class="identity__title">Manager</p>
      <p class="identity__address">1480 Alder Lane<br>Suite 210, Lakeview, IN 46000</p>
    </div>
    <ul class="contacts">
      <li>
        <svg viewBox="0 0 24 24" aria-hidden="true"><path fill="#111" d="M6.6 10.8a15.1 15.1 0 0 0 6.6 6.6l2.2-2.2c.3-.3.7-.4 1-.2 1.1.4 2.3.6 3.6.6.6 0 1 .4 1 1V20c0 .6-.4 1-1 1A17 17 0 0 1 3 4c0-.6.4-1 1-1h3.5c.6 0 1 .4 1 1 0 1.3.2 2.5.6 3.6.1.3 0 .7-.2 1z"/></svg>
        (555) 014-2278
      </li>
      <li>
        <svg viewBox="0 0 24 24" aria-hidden="true"><rect x="2" y="5" width="20" height="14" fill="#111"/><path d="M2 5l10 8 10-8M2 19l8-7M22 19l-8-7" stroke="#fff" stroke-width="1.4" fill="none"/></svg>
        info@northfieldinjurylawyers.com
      </li>
      <li>
        <svg viewBox="0 0 24 24" aria-hidden="true"><g fill="none" stroke="#111" stroke-width="1.6"><circle cx="12" cy="12" r="9.5"/><ellipse cx="12" cy="12" rx="4" ry="9.5"/><path d="M2.5 12h19M4 7h16M4 17h16"/></g></svg>
        www.northfieldinjurylawyers.com
      </li>
    </ul>
  </section>

  <section class="card card--back" aria-label="Business card back">
    <div class="brand">
      <span class="brand__square" aria-hidden="true"></span>
      <span class="brand__name">Northfield Injury Lawyers</span>
    </div>
  </section>
</main>
</body>
</html>
```